Logo and business card design

I would like a logo and business card designed for a bookkeeping business called "Meridel Accounting"
Would like the submission to be an editable file.

Info for business card:

Rowan Pell, CPA, CGA
President
rowanpell@mail
555.318.4062
Toronto, ON

```html
<!DOCTYPE html>
<html lang="en">
<head>
<meta charset="utf-8">
<title>Meridel Accounting — Business Card</title>
<link href="https://fonts.googleapis.com/css2?family=Lato:wght@400;700;900&display=swap" rel="stylesheet">
<style>
  :root {
    --backdrop: #3b3b3d;
    --card-black: #141414;
    --panel-black: #1c1c1c;
    --accent-orange: #f7941d;
    --text-white: #ffffff;
    --text-muted: #d9d9d9;
  }
  html, body {
    margin: 0;
    padding: 0;
    width: 1200px;
    height: 744px;
    overflow: hidden;
    background: var(--backdrop);
  }
  .canvas {
    width: 1200px;
    height: 744px;
    display: flex;
    align-items: center;
    justify-content: center;
    gap: 40px;
  }
  .card {
    width: 540px;
    height: 310px;
    display: block;
    box-shadow: 0 14px 30px rgba(0,0,0,0.45);
    font-family: 'Lato', sans-serif;
  }
  .card-bg { fill: var(--card-black); }
  .accent-band { fill: var(--accent-orange); }
  .hex-panel { fill: var(--panel-black); }
  .brand-name {
    fill: var(--text-white);
    font-weight: 900;
    font-size: 20px;
    letter-spacing: 1px;
  }
  .person-name {
    fill: var(--text-white);
    font-weight: 700;
    font-size: 19px;
  }
  .person-credentials { font-weight: 400; }
  .person-title {
    fill: var(--accent-orange);
    font-weight: 400;
    font-size: 13px;
  }
  .rule-white { stroke: var(--text-white); stroke-width: 1.5; }
  .rule-orange { stroke: var(--accent-orange); stroke-width: 3; }
  .contact-text {
    fill: var(--text-muted);
    font-size: 12.5px;
    font-weight: 400;
  }
  .contact-icon { fill: var(--text-white); }
</style>
</head>
<body>
<main class="canvas">

  <!-- Front of card -->
  <svg class="card card-front" viewBox="0 0 540 310" role="img" aria-label="Meridel Accounting card front">
    <defs>
      <filter id="hex-shadow-front" x="-30%" y="-30%" width="160%" height="160%">
        <feDropShadow dx="-4" dy="6" stdDeviation="7" flood-color="#000" flood-opacity="0.6"/>
      </filter>
    </defs>
    <rect class="card-bg" width="540" height="310"/>
    <polygon class="accent-band" points="290,0 540,0 540,310 350,310"/>
    <polygon class="hex-panel" filter="url(#hex-shadow-front)"
      points="395,25 500,87.5 500,212.5 395,275 290,212.5 290,87.5"/>
    <text class="brand-name" x="395" y="148" text-anchor="middle">MERIDEL</text>
    <text class="brand-name" x="395" y="172" text-anchor="middle">ACCOUNTING</text>
  </svg>

  <!-- Back of card -->
  <svg class="card card-back" viewBox="0 0 540 310" role="img" aria-label="Rowan Pell contact details">
    <defs>
      <filter id="hex-shadow-back" x="-30%" y="-30%" width="160%" height="160%">
        <feDropShadow dx="4" dy="6" stdDeviation="7" flood-color="#000" flood-opacity="0.6"/>
      </filter>
    </defs>
    <rect class="card-bg" width="540" height="310"/>
    <polygon class="accent-band" points="0,0 200,0 250,310 0,310"/>
    <polygon class="hex-panel" filter="url(#hex-shadow-back)"
      points="185,35 290,95 290,215 185,275 80,215 80,95"/>

    <text class="person-name" x="185" y="152" text-anchor="middle">Rowan Pell<tspan class="person-credentials">, CPA, CGA</tspan></text>
    <text class="person-title" x="185" y="170" text-anchor="middle">President</text>
    <line class="rule-white" x1="150" y1="180" x2="282" y2="180"/>
    <line class="rule-orange" x1="95" y1="186" x2="140" y2="186"/>

    <!-- location -->
    <g class="contact-row">
      <path class="contact-icon" d="M335 110 a5 5 0 0 1 10 0 c0 4 -5 9 -5 9 s-5 -5 -5 -9z M340 108 a1.8 1.8 0 1 0 0.01 0z" fill-rule="evenodd"/>
      <text class="contact-text" x="356" y="117">Toronto, ON</text>
    </g>
    <!-- phone -->
    <g class="contact-row">
      <path class="contact-icon" d="M336 138 c1 -1 3 -1 3.5 0 l1.5 2.5 c0.5 1 0 2 -1 2.5 c0.8 2 2.5 3.7 4.5 4.5 c0.5 -1 1.5 -1.5 2.5 -1 l2.5 1.5 c1 0.5 1 2.5 0 3.5 c-2 2 -5 1.5 -8 -1 c-3 -2.5 -6 -6 -6.5 -9 c-0.3 -1.5 0 -2.8 1 -3.5z"/>
      <text class="contact-text" x="356" y="149">555.318.4062</text>
    </g>
    <!-- email -->
    <g class="contact-row">
      <rect class="contact-icon" x="334" y="172" width="13" height="9" rx="1"/>
      <polyline points="334.5,172.5 340.5,177.5 346.5,172.5" fill="none" stroke="#141414" stroke-width="1.2"/>
      <text class="contact-text" x="356" y="181">rowanpell@mail</text>
    </g>
  </svg>

</main>
</body>
</html>
```